8"x5" postcard for Wireless Internet introduction to new mountain town market

I need to market high speed internet to a resort mountain town without doing the obvious laptop on a mountain top thing, so tired. We are going to be competing directly with another provider with same cost, but we will be offering free installation. The area is Aspen Colorado, so the clientele are outdoor types who have suffered for years from being disconnected in their mountain town. We offer fast internet and excellent customer service from people who live in their neck of the woods.

Target Market(s)

23-55 years old, both resort living, families and ski bums

Font styles to use
Sans Serif

Colors

Designer to choose colors to be used in the design.

Requirements
Must have
• Visual appeal and fresh verbiage. We don't mind being a little edgy. We are a young company and we want to appeal to people looking for a provider who gets them. We prefer a clean look.
Nice to have
• Nice to have colors that match our logo
Should not have
• stuffy concepts or verbiage that is too much like a car salesman. We don't want to look like a 'big box' company.

```html
<!DOCTYPE html>
<html lang="en">
<head>
<meta charset="utf-8">
<title>Summit Loop Broadband – High Speed Internet Postcard</title>
<link rel="stylesheet" href="https://fonts.googleapis.com/css2?family=Open+Sans:wght@700;800&family=PT+Sans:wght@400;700&display=swap">
<style>
  :root {
    --backdrop: #e4e0dc;
    --ink-dark: #444446;
    --panel-dark: #47464a;
    --text-dark: #3a3a3c;
    --white: #ffffff;
    --yellow: #fdd33b;
    --yellow-warm: #fbc43e;
    --orange: #f5a93c;
    --olive: #b99a34;
    --sky: #bcc7cd;
    --haze: #9c9e99;
    --forest: #4d4f45;
  }
  html, body {
    margin: 0;
    width: 1200px;
    height: 1200px;
    overflow: hidden;
    background: var(--backdrop);
  }
  .canvas {
    width: 1200px;
    height: 1200px;
    display: flex;
    align-items: center;
    justify-content: center;
  }
  .postcard {
    width: 688px;
    height: 1100px;
    display: block;
    box-shadow: 0 6px 18px rgba(0,0,0,0.25);
  }
  .brand-name { font-family: "Open Sans", sans-serif; font-weight: 800; fill: var(--ink-dark); font-size: 30px; }
  .headline { font-family: "Open Sans", sans-serif; font-weight: 800; font-size: 68px; fill: var(--white); stroke: var(--ink-dark); stroke-width: 2.5px; paint-order: stroke; }
  .tagline { font-family: "Open Sans", sans-serif; font-weight: 700; font-size: 31px; fill: var(--white); }
  .feature { font-family: "PT Sans", sans-serif; font-size: 27px; fill: var(--text-dark); }
  .price { font-family: "PT Sans", sans-serif; font-size: 48px; fill: var(--text-dark); }
  .call-now { font-family: "PT Sans", sans-serif; font-weight: 700; font-size: 34px; fill: var(--white); }
  .contact { font-family: "PT Sans", sans-serif; font-size: 27px; fill: var(--text-dark); }
</style>
</head>
<body>
<main class="canvas">
  <svg class="postcard" viewBox="0 0 805 1287" xmlns="http://www.w3.org/2000/svg">
    <defs>
      <linearGradient id="photo-tones" x1="0" y1="0" x2="0" y2="1">
        <stop offset="0" stop-color="var(--sky)"/>
        <stop offset="0.5" stop-color="var(--haze)"/>
        <stop offset="0.75" stop-color="var(--forest)"/>
        <stop offset="1" stop-color="#6a5f4c"/>
      </linearGradient>
      <linearGradient id="offer-panel" x1="0.1" y1="1" x2="0.9" y2="0">
        <stop offset="0" stop-color="var(--olive)"/>
        <stop offset="0.35" stop-color="var(--yellow-warm)"/>
        <stop offset="1" stop-color="var(--orange)"/>
      </linearGradient>
      <linearGradient id="contact-panel" x1="0" y1="0" x2="1" y2="0">
        <stop offset="0" stop-color="var(--yellow)"/>
        <stop offset="1" stop-color="var(--yellow-warm)"/>
      </linearGradient>
    </defs>

    <!-- Hero photo area -->
    <g class="hero-photo" role="img" aria-label="Photo of a hiker leaping over a rocky mountain ledge above a forested valley at dusk">
      <rect x="0" y="0" width="805" height="800" fill="url(#photo-tones)"/>
    </g>
    <rect class="headline-veil" x="414" y="0" width="391" height="760" fill="rgba(50,50,52,0.22)"/>

    <!-- Top right corner accent -->
    <polygon class="corner-accent" points="410,0 805,0 805,112" fill="var(--yellow-warm)"/>
    <line class="corner-stripe" x1="388" y1="-4" x2="810" y2="128" stroke="var(--white)" stroke-width="11"/>
    <polygon class="corner-block" points="742,0 805,0 805,80 742,55" fill="var(--panel-dark)"/>

    <!-- Brand -->
    <circle class="brand-dot" cx="66" cy="72" r="32" fill="var(--yellow-warm)"/>
    <text class="brand-name" x="110" y="70">SUMMIT LOOP</text>
    <text class="brand-name" x="110" y="104">BROADBAND</text>

    <!-- Headline -->
    <text class="headline" x="770" y="200" text-anchor="end">HIGH</text>
    <text class="headline" x="770" y="273" text-anchor="end">SPEED</text>
    <text class="headline" x="770" y="346" text-anchor="end">INTERNET</text>
    <rect class="headline-rule" x="456" y="369" width="314" height="6" fill="var(--panel-dark)"/>
    <rect class="headline-rule" x="456" y="378" width="314" height="6" fill="var(--yellow-warm)"/>

    <!-- Lower panels -->
    <polygon class="contact-panel" points="805,760 805,1287 0,1287 0,1260" fill="url(#contact-panel)"/>
    <polygon class="offer-panel" points="40,540 805,750 805,758 20,1290 40,1290" fill="url(#offer-panel)"/>
    <polygon class="side-band" points="0,520 65,538 65,1190 0,1240" fill="var(--panel-dark)"/>
    <line class="divider-stripe" x1="-5" y1="518" x2="810" y2="752" stroke="var(--white)" stroke-width="12"/>
    <line class="divider-stripe" x1="812" y1="758" x2="8" y2="1295" stroke="var(--white)" stroke-width="13"/>
    <polygon class="side-band" points="805,848 742,888 742,1287 805,1287" fill="var(--panel-dark)"/>

    <circle class="accent-dot" cx="648" cy="782" r="33" fill="var(--panel-dark)"/>

    <!-- Offer copy -->
    <text class="tagline" x="95" y="663">Better,</text>
    <text class="tagline" x="95" y="706">Not Bigger!</text>

    <text class="feature" x="95" y="790">Free residential Installation</text>
    <text class="feature" x="95" y="832">In-House Tech Support</text>
    <text class="feature" x="95" y="875">10, 25 and 40Mbps</text>

    <text class="feature" x="95" y="960">Prices start at</text>
    <text class="price" x="95" y="1022">$59.95</text>

    <!-- Contact -->
    <text class="call-now" x="710" y="1024" text-anchor="end">Call Now</text>
    <text class="contact" x="710" y="1110" text-anchor="end">1 888 555 0142</text>
    <text class="contact" x="710" y="1152" text-anchor="end">1 970 555 0187</text>
    <text class="contact" x="710" y="1194" text-anchor="end">www.summitloop.net/peaks</text>
    <text class="contact" x="710" y="1236" text-anchor="end">peaks@summitloopbroadband.com</text>
  </svg>
</main>
</body>
</html>
```